Slide Master for Harrowfield Engines - A Systematic Hedge Fund

We are looking for someone to produce a theme and slide master for us for our investor presentations. I have uploaded a few examples of templates that we would like to have included:
Main Title
Section Title
Slides with just bullet points
Different image/table configurations with bullet points and foot notes
Biographies of different lengths
A disclaimer (no one will read this but it should still look nice and needs to be in the presentations)
I have also uploaded the company logo, business card and colour definitions. Currently we have a blue colour scheme defined, but it would be nice to get a complementary set of colours so that when we have charts with more elements we can just draw from those.
The most important thing is that the slide master must be of general use to us. We arn't looking to have a specific presentation designed for us, but a theme/style that we can apply ourselves to any presentation we need to give in the future. It should have clearly defined guidelines for where content should go (and if this is different with and without footnotes for example). We would also like it to have a similar feel to the logo/business cards, so matt colours, high contrast, but not busy.
I'm excited to see the results!

```html
<!DOCTYPE html>
<html lang="en">
<head>
<meta charset="utf-8">
<title>Harrowfield Engines – Slide Master</title>
<link href="https://fonts.googleapis.com/css2?family=Roboto:wght@400;500;700;900&family=Montserrat:wght@300;400;500;600&display=swap" rel="stylesheet">
<style>
:root{
  --stage:#454345;
  --navy:#0b4a80;
  --navy-deep:#073a6a;
  --ink:#1f2a36;
  --grey:#6d7680;
  --blue:#4f8fd9;
  --blue-light:#b9d3ee;
  --band:#c6dbf2;
  --rule:#dfe6ee;
  --photo-a:#8aa6c2;
  --photo-b:#2e5a86;
  --dark-wedge:#232323;
}
*{margin:0;padding:0;box-sizing:border-box}
html,body{width:1200px;height:2402px;overflow:hidden;background:var(--stage)}
body{position:relative;font-family:"Montserrat",sans-serif;color:var(--ink)}
.slide{position:absolute;width:540px;height:303px;overflow:hidden;background:#fff}
.slide-hero{left:187px;top:108px;transform:scale(1.53);transform-origin:0 0}
.abs{position:absolute}
.brand{font-family:"Roboto",sans-serif;font-weight:700;color:var(--navy);text-transform:uppercase;line-height:1.05;letter-spacing:.04em}
.slide-title{position:absolute;left:0;right:0;text-align:center;font-family:"Roboto",sans-serif;font-weight:500;font-size:22px;color:#2a2f35;letter-spacing:-.01em}
.slide-sub{position:absolute;left:0;right:0;text-align:center;font-size:7.5px;color:#3b4450}
.foot{position:absolute;left:0;right:0;bottom:11px;height:16px}
.foot .brand{position:absolute;left:11px;top:0;font-size:7px}
.foot-rule{position:absolute;left:95px;top:2px;width:3px;height:13px;background:var(--navy)}
.foot-band{position:absolute;left:100px;right:0;top:3px;height:11px;background:var(--band);font-size:5px;color:var(--navy);line-height:11px}
.foot-band .note{position:absolute;left:10px}
.foot-band .circ{position:absolute;right:30px}
.foot-band .num{position:absolute;right:11px;font-weight:600}
.body-text{font-size:4.6px;line-height:1.3;text-align:justify;color:#333d48}
.body-text p+p{margin-top:5px}
.photo{position:absolute;inset:0}
/* title slide */
.hero-title{position:absolute;left:52px;top:120px;color:#fff;font-family:"Roboto",sans-serif;font-weight:700;font-size:30px;line-height:1.08;letter-spacing:-.035em}
.hero-sub{position:absolute;left:52px;top:196px;color:#fff;font-weight:300;font-size:15px;line-height:1.15}
.hero-date{position:absolute;left:52px;top:243px;color:#fff;font-size:5.8px}
.hero-copy{position:absolute;left:264px;top:283px;color:#8a9098;font-size:4.6px}
/* cards */
.card{position:absolute;top:122px;width:232px}
.card-head{height:19px;border-radius:10px 10px 10px 0;background:var(--blue);color:#fff;font-family:"Roboto",sans-serif;font-weight:700;font-size:10px;line-height:19px;padding-left:18px}
.card-list{margin:8px 0 0 0;border-left:1px solid var(--rule);padding-left:18px;list-style:none}
.card-list li{font-size:6.8px;line-height:14px;color:#333d48;position:relative}
.card-list li:before{content:"";position:absolute;left:-8px;top:6px;width:2.5px;height:2.5px;border-radius:50%;background:#333d48}
.ticks{list-style:none}
.ticks li{position:relative;padding-left:7px}
.ticks li:before{content:"";position:absolute;left:0;top:.55em;width:2.4px;height:2.4px;border-radius:50%;background:currentColor}
.sub-head{font-family:"Roboto",sans-serif;font-weight:500;font-size:9px;color:var(--navy)}
.footnote{position:absolute;font-size:4.3px;line-height:1.25;color:#333d48}
table.grid{border-collapse:collapse;width:100%;font-size:5px}
table.grid th{background:var(--blue);color:#fff;font-weight:400;text-align:left;padding:0 3px;height:14px;border-right:1px solid #fff}
table.grid td{height:14.7px;border:1px solid var(--rule)}
.contact{position:absolute;left:58px;color:#fff}
.contact-row{display:flex;align-items:center;gap:8px;font-size:6.6px;height:15px}
</style>
</head>
<body>

<!-- Title slide (featured) -->
<section class="slide slide-hero" aria-label="Title slide">
  <div class="photo" role="img" aria-label="Photograph of a business person holding a pen and a tablet"
       style="left:272px;background:linear-gradient(135deg,var(--photo-a),#d6e1ec 55%,#9fb5ca)"></div>
  <svg class="abs" width="540" height="303" viewBox="0 0 540 303" style="left:0;top:0">
    <polygon points="0,0 272,0 303,0 325,94 0,94" fill="#fff"/>
    <polygon points="0,94 375,94 450,273 0,273" fill="var(--navy)"/>
    <polygon points="375,94 450,273 520,273 400,94" fill="var(--navy)" opacity=".45"/>
    <polygon points="0,215 48,303 0,303" fill="var(--dark-wedge)"/>
    <polygon points="40,273 450,273 470,303 56,303" fill="#fff"/>
  </svg>
  <div class="brand abs" style="left:28px;top:42px;font-size:13px">Harrowfield<br>Engines</div>
  <div class="hero-title">Presentations<br>Title Goes Here!</div>
  <div class="hero-sub">Subtitle of Presentation<br>Goes Here!</div>
  <div class="hero-date">Friday, June 4, 2021</div>
  <div class="hero-copy">© 2021 Harrowfield Engines. All rights reserved.</div>
</section>

<!-- 1: Title -->
<section class="slide" style="left:51px;top:751px" aria-label="Title slide">
  <div class="photo" role="img" aria-label="Photograph of a business person holding a pen and a tablet"
       style="left:272px;background:linear-gradient(135deg,var(--photo-a),#d6e1ec 55%,#9fb5ca)"></div>
  <svg class="abs" width="540" height="303" viewBox="0 0 540 303" style="left:0;top:0">
    <polygon points="0,0 303,0 325,94 0,94" fill="#fff"/>
    <polygon points="0,94 375,94 450,273 0,273" fill="var(--navy)"/>
    <polygon points="375,94 450,273 520,273 400,94" fill="var(--navy)" opacity=".45"/>
    <polygon points="0,215 48,303 0,303" fill="var(--dark-wedge)"/>
    <polygon points="40,273 450,273 470,303 56,303" fill="#fff"/>
  </svg>
  <div class="brand abs" style="left:28px;top:42px;font-size:13px">Harrowfield<br>Engines</div>
  <div class="hero-title">Presentations<br>Title Goes Here!</div>
  <div class="hero-sub">Subtitle of Presentation<br>Goes Here!</div>
  <div class="hero-date">Friday, June 4, 2021</div>
  <div class="hero-copy">© 2021 Harrowfield Engines. All rights reserved.</div>
</section>

<!-- 2: Disclaimer -->
<section class="slide" style="left:609px;top:751px" aria-label="Disclaimer">
  <div class="slide-title" style="top:34px">Disclaimer</div>
  <div class="body-text abs" style="left:32px;top:84px;width:146px">
    <p>Lorem ipsum dolor sit amet, consectetur adipiscing elit. Vestibulum lacinia eros eu pharetra mollis. Nullam vulputate purus mi, sed maximus est sodales mollis. Mauris nec vulputate eros. Cras lectus lacus, lacinia eu dapibus ac, tincidunt eu nisi. Suspendisse in volutpat risus. Nunc pharetra porttitor lorem. Vivamus at lectus sit amet lacus dictum tincidunt at vel magna. Donec blandit nulla ac erat condimentum, fringilla feugiat ex porttitor. Proin est odio, suscipit vitae magna at, bibendum tincidunt mi. Aenean facilisis pharetra lacus sed tempus. Nam finibus eu diam eu consectetur.</p>
    <p>Lorem ipsum dolor sit amet, consectetur adipiscing elit. Vestibulum lacinia eros eu pharetra mollis. Nullam vulputate purus mi, sed maximus est sodales mollis. Mauris nec vulputate eros. Cras lectus lacus, lacinia eu dapibus ac, tincidunt eu nisi. Suspendisse in volutpat.</p>
  </div>
  <div class="body-text abs" style="left:197px;top:84px;width:146px">
    <p>Lorem ipsum dolor sit amet, consectetur adipiscing elit. Vestibulum lacinia eros eu pharetra mollis. Nullam vulputate purus mi, sed maximus est sodales mollis. Mauris nec vulputate eros. Cras lectus lacus, lacinia eu dapibus ac, tincidunt eu nisi. Suspendisse in volutpat risus. Nunc pharetra porttitor lorem. Vivamus at lectus sit amet lacus dictum tincidunt at vel magna. Donec blandit nulla ac erat condimentum, fringilla feugiat ex porttitor. Proin est odio, suscipit vitae magna at, bibendum tincidunt mi. Aenean facilisis pharetra lacus sed tempus. Nam finibus eu diam eu consectetur.</p>
    <p>Lorem ipsum dolor sit amet, consectetur adipiscing elit. Vestibulum lacinia eros eu pharetra mollis. Nullam vulputate purus mi, sed maximus est sodales mollis. Mauris nec vulputate eros. Cras lectus lacus, lacinia eu dapibus ac, tincidunt eu nisi. Suspendisse in volutpat risus.</p>
  </div>
  <div class="body-text abs" style="left:361px;top:84px;width:146px">
    <p>Lorem ipsum dolor sit amet, consectetur adipiscing elit. Vestibulum lacinia eros eu pharetra mollis. Nullam vulputate purus mi, sed maximus est sodales mollis. Mauris nec vulputate eros. Cras lectus lacus, lacinia eu dapibus ac, tincidunt eu nisi. Suspendisse in volutpat.</p>
    <p>Lorem ipsum dolor sit amet, consectetur adipiscing elit. Vestibulum lacinia eros eu pharetra mollis. Nullam vulputate purus mi, sed maximus est sodales mollis. Mauris nec vulputate eros. Cras lectus lacus, lacinia eu dapibus ac, tincidunt eu nisi. Suspendisse in volutpat risus. Nunc pharetra porttitor lorem. Vivamus at lectus sit amet lacus dictum tincidunt at vel magna. Donec blandit nulla ac erat condimentum, fringilla feugiat ex porttitor. Proin est odio, suscipit vitae magna at, bibendum tincidunt mi. Aenean facilisis pharetra lacus sed tempus. Nam finibus eu diam eu consectetur.</p>
  </div>
  <div class="foot"><span class="brand">Harrowfield<br>Engines</span><i class="foot-rule"></i><div class="foot-band"><span class="circ">Not For Circulation</span><span class="num">2</span></div></div>
</section>

<!-- 3: Section title -->
<section class="slide" style="left:51px;top:1072px" aria-label="Section title slide">
  <div class="photo" role="img" aria-label="Photograph of colleagues reviewing charts on a tablet"
       style="background:linear-gradient(120deg,#33506f,#8ea6bd 45%,#c9d4df 70%,#5b7696)"></div>
  <svg class="abs" width="540" height="303" viewBox="0 0 540 303" style="left:0;top:0">
    <polygon points="0,94 300,94 380,270 0,270" fill="var(--navy)" opacity=".93"/>
    <polygon points="300,94 380,270 420,270 340,94" fill="var(--navy)" opacity=".45"/>
  </svg>
  <div class="abs" style="left:39px;top:160px;color:#fff;font-family:'Roboto',sans-serif;font-weight:700;font-size:28px;line-height:1.1;letter-spacing:-.035em">Section Title<br>Goes Here!</div>
  <div class="abs" style="left:39px;top:232px;color:#fff;font-weight:300;font-size:15px">Subtitle of Section</div>
</section>

<!-- 4: Bullet cards -->
<section class="slide" style="left:609px;top:1072px" aria-label="Slide with two bullet lists">
  <div class="slide-title" style="top:36px">Slide Title Goes Here!</div>
  <div class="slide-sub" style="top:64px">Subtitle of Slide Goes Here!</div>
  <div class="card" style="left:30px">
    <div class="card-head">Title Goes Here!</div>
    <ul class="card-list"><li>Lorem ipsum dolor sit amet.</li><li>Vestibulum lacinia eros eu pharetra mollis.</li><li>Nullam vulputate purus mi.</li><li>Mauris nec vulputate eros.</li><li>Vestibulum lacinia eros eu pharetra mollis.</li></ul>
  </div>
  <div class="card" style="left:280px">
    <div class="card-head">Title Goes Here!</div>
    <ul class="card-list"><li>Lorem ipsum dolor sit amet.</li><li>Vestibulum lacinia eros eu pharetra mollis.</li><li>Nullam vulputate purus mi.</li><li>Mauris nec vulputate eros.</li><li>Vestibulum lacinia eros eu pharetra mollis.</li></ul>
  </div>
  <div class="foot"><span class="brand">Harrowfield<br>Engines</span><i class="foot-rule"></i><div class="foot-band"><span class="circ">Not For Circulation</span><span class="num">4</span></div></div>
</section>

<!-- 5: Charts -->
<section class="slide" style="left:51px;top:1394px" aria-label="Slide with two bar charts">
  <div class="slide-title" style="top:36px">Slide Title Goes Here!</div>
  <div class="slide-sub" style="top:64px">Subtitle of Slide Goes Here!</div>
  <div class="abs" style="left:0;right:0;top:87px;height:37px;background:var(--blue);color:#fff;font-size:5.6px;line-height:1.2">
    <ul class="ticks abs" style="left:34px;top:8px;width:220px"><li>Lorem ipsum dolor sit amet, consectetur adipiscing elit</li><li>Lorem ipsum dolor sit amet, consectetur adipiscing elit. Vestibulum lacinia eros eu pharetra mollis.</li></ul>
    <i class="abs" style="left:270px;top:6px;width:1px;height:25px;background:#fff"></i>
    <ul class="ticks abs" style="left:284px;top:8px;width:230px"><li>Mauris nec vulputate eros. Cras lectus lacus, lacinia eu dapibus ac, tincidunt eu nisi.</li><li>Lorem ipsum dolor sit amet, consectetur adipiscing elit.</li></ul>
  </div>
  <svg class="abs" style="left:22px;top:137px" width="240" height="125" viewBox="0 0 240 125" font-family="Montserrat, sans-serif" font-size="5" fill="#555">
    <text x="135" y="7" text-anchor="middle" font-size="6">Chart Title</text>
    <g stroke="#e4e8ec" stroke-width=".5"><line x1="20" y1="19" x2="240" y2="19"/><line x1="20" y1="34" x2="240" y2="34"/><line x1="20" y1="49" x2="240" y2="49"/><line x1="20" y1="64" x2="240" y2="64"/><line x1="20" y1="79" x2="240" y2="79"/><line x1="20" y1="94" x2="240" y2="94"/><line x1="20" y1="109" x2="240" y2="109"/></g>
    <g text-anchor="end"><text x="14" y="21">6</text><text x="14" y="36">5</text><text x="14" y="51">4</text><text x="14" y="66">3</text><text x="14" y="81">2</text><text x="14" y="96">1</text><text x="14" y="111">0</text></g>
    <g fill="var(--navy)"><rect x="34" y="45" width="9" height="64"/><rect x="88" y="72" width="9" height="37"/><rect x="142" y="56" width="9" height="53"/><rect x="196" y="42" width="9" height="67"/></g>
    <g fill="var(--blue)"><rect x="45" y="73" width="9" height="36"/><rect x="99" y="43" width="9" height="66"/><rect x="153" y="82" width="9" height="27"/><rect x="207" y="67" width="9" height="42"/></g>
    <g fill="var(--blue-light)"><rect x="56" y="79" width="9" height="30"/><rect x="110" y="79" width="9" height="30"/><rect x="164" y="64" width="9" height="45"/><rect x="218" y="34" width="9" height="75"/></g>
    <g text-anchor="middle"><text x="50" y="122">Category 1</text><text x="104" y="122">Category 2</text><text x="158" y="122">Category 3</text><text x="212" y="122">Category 4</text></g>
  </svg>
  <svg class="abs" style="left:268px;top:137px" width="240" height="125" viewBox="0 0 240 125" font-family="Montserrat, sans-serif" font-size="5" fill="#555">
    <text x="135" y="7" text-anchor="middle" font-size="6">Chart Title</text>
    <g stroke="#e4e8ec" stroke-width=".5"><line x1="20" y1="19" x2="240" y2="19"/><line x1="20" y1="34" x2="240" y2="34"/><line x1="20" y1="49" x2="240" y2="49"/><line x1="20" y1="64" x2="240" y2="64"/><line x1="20" y1="79" x2="240" y2="79"/><line x1="20" y1="94" x2="240" y2="94"/><line x1="20" y1="109" x2="240" y2="109"/></g>
    <g text-anchor="end"><text x="14" y="21">6</text><text x="14" y="36">5</text><text x="14" y="51">4</text><text x="14" y="66">3</text><text x="14" y="81">2</text><text x="14" y="96">1</text><text x="14" y="111">0</text></g>
    <g fill="var(--navy)"><rect x="34" y="45" width="9" height="64"/><rect x="88" y="72" width="9" height="37"/><rect x="142" y="56" width="9" height="53"/><rect x="196" y="42" width="9" height="67"/></g>
    <g fill="var(--blue)"><rect x="45" y="73" width="9" height="36"/><rect x="99" y="43" width="9" height="66"/><rect x="153" y="82" width="9" height="27"/><rect x="207" y="67" width="9" height="42"/></g>
    <g fill="var(--blue-light)"><rect x="56" y="79" width="9" height="30"/><rect x="110" y="79" width="9" height="30"/><rect x="164" y="64" width="9" height="45"/><rect x="218" y="34" width="9" height="75"/></g>
    <g text-anchor="middle"><text x="50" y="122">Category 1</text><text x="104" y="122">Category 2</text><text x="158" y="122">Category 3</text><text x="212" y="122">Category 4</text></g>
  </svg>
  <div class="foot"><span class="brand">Harrowfield<br>Engines</span><i class="foot-rule"></i><div class="foot-band"><span class="note">Footnote Goes Here</span><span class="circ">Not For Circulation</span><span class="num">5</span></div></div>
</section>

<!-- 6: Table -->
<section class="slide" style="left:609px;top:1394px" aria-label="Slide with a table and footnote">
  <div class="slide-title" style="top:36px">Slide Title Goes Here!</div>
  <div class="slide-sub" style="top:64px">Subtitle of Slide Goes Here!</div>
  <div class="abs" style="left:33px;top:84px;font-size:10px;color:#333d48">Table With A Footnote*</div>
  <div class="abs" style="left:28px;top:100px;width:347px">
    <table class="grid">
      <tr><th style="width:75px">Title 1</th><th>Title 2</th><th>Title 3</th><th>Title 4</th><th>Title 5</th><th>Title 6</th><th>Title 7</th><th>Title 8</th></tr>
      <tr><td></td><td></td><td></td><td></td><td></td><td></td><td></td><td></td></tr>
      <tr><td></td><td></td><td></td><td></td><td></td><td></td><td></td><td></td></tr>
      <tr><td></td><td></td><td></td><td></td><td></td><td></td><td></td><td></td></tr>
      <tr><td></td><td></td><td></td><td></td><td></td><td></td><td></td><td></td></tr>
      <tr><td></td><td></td><td></td><td></td><td></td><td></td><td></td><td></td></tr>
      <tr><td></td><td></td><td></td><td></td><td></td><td></td><td></td><td></td></tr>
      <tr><td></td><td></td><td></td><td></td><td></td><td></td><td></td><td></td></tr>
      <tr><td></td><td></td><td></td><td></td><td></td><td></td><td></td><td></td></tr>
    </table>
  </div>
  <div class="abs" style="left:381px;top:100px;width:130px;height:137px;background:var(--blue);color:#fff;font-size:6.8px;line-height:1.2;padding:12px 10px 0 13px">
    <ul class="ticks"><li>Lorem ipsum dolor sit amet, consectetur adipiscing elit.</li><li style="margin-top:7px">Vestibulum lacinia eros eu pharetra mollis. Nullam vulputate purus mi, sed maximus est sodales mollis.</li><li style="margin-top:7px">Mauris nec vulputate eros. Cras lectus lacus, lacinia eu dapibus ac, tincidunt eu nisi.</li></ul>
  </div>
  <div class="footnote" style="left:32px;top:253px;width:480px">* Lorem ipsum dolor sit amet, consectetur adipiscing elit. Vestibulum lacinia eros eu pharetra mollis. Nullam vulputate purus mi, sed maximus est sodales mollis. Mauris nec vulputate eros. Cras lectus lacus, lacinia. Lorem ipsum dolor sit amet, consectetur adipiscing elit. Vestibulum lacinia eros eu pharetra mollis.</div>
  <div class="foot"><span class="brand">Harrowfield<br>Engines</span><i class="foot-rule"></i><div class="foot-band"><span class="circ">Not For Circulation</span><span class="num">6</span></div></div>
</section>

<!-- 7: Text and line chart -->
<section class="slide" style="left:51px;top:1716px" aria-label="Slide with text and a line chart">
  <div class="slide-title" style="top:36px">Slide Title Goes Here!</div>
  <div class="slide-sub" style="top:64px">Subtitle of Slide Goes Here!</div>
  <div class="abs" style="left:33px;top:100px;width:220px">
    <div class="sub-head">Title Goes Here!</div>
    <p style="font-size:6.8px;line-height:1.2;color:#333d48;margin-top:3px">Lorem ipsum dolor sit amet, consectetur adipiscing elit. Vestibulum lacinia eros eu pharetra mollis. Nullam vulputate purus mi, sed maximus est sodales mollis. Mauris nec vulputate eros.</p>
    <div class="sub-head" style="margin-top:22px">Title Goes Here!</div>
    <p style="font-size:6.8px;line-height:1.2;color:#333d48;margin-top:3px">Lorem ipsum dolor sit amet, consectetur adipiscing elit. Vestibulum lacinia eros eu pharetra mollis. Nullam vulputate purus mi, sed maximus est sodales mollis. Mauris nec vulputate eros.</p>
  </div>
  <svg class="abs" style="left:270px;top:95px" width="245" height="140" viewBox="0 0 245 140" font-family="Montserrat, sans-serif" font-size="5" fill="#555">
    <g stroke="#e4e8ec" stroke-width=".5"><line x1="30" y1="5" x2="240" y2="5"/><line x1="30" y1="19" x2="240" y2="19"/><line x1="30" y1="33" x2="240" y2="33"/><line x1="30" y1="47" x2="240" y2="47"/><line x1="30" y1="61" x2="240" y2="61"/><line x1="30" y1="75" x2="240" y2="75"/><line x1="30" y1="89" x2="240" y2="89"/><line x1="30" y1="103" x2="240" y2="103"/><line x1="30" y1="117" x2="240" y2="117"/><line x1="30" y1="131" x2="240" y2="131"/></g>
    <g text-anchor="end"><text x="25" y="7">450</text><text x="25" y="21">400</text><text x="25" y="35">350</text><text x="25" y="49">300</text><text x="25" y="63">250</text><text x="25" y="77">200</text><text x="25" y="91">150</text><text x="25" y="105">100</text><text x="25" y="119">50</text><text x="25" y="133">0</text></g>
    <g text-anchor="middle"><text x="30" y="139">0</text><text x="65" y="139">2</text><text x="100" y="139">4</text><text x="135" y="139">6</text><text x="170" y="139">8</text><text x="205" y="139">10</text><text x="240" y="139">12</text></g>
    <path d="M38 128 C70 118 100 108 135 75 C155 45 160 10 172 12 C185 14 190 35 210 30" fill="none" stroke="var(--blue)" stroke-width="1"/>
    <path d="M38 129 C60 120 75 108 90 115 C110 120 120 80 135 85 C145 90 150 120 158 118 C170 110 185 110 210 100" fill="none" stroke="var(--navy)" stroke-width="1"/>
  </svg>
  <div class="footnote" style="left:33px;top:246px;width:480px">* Lorem ipsum dolor sit amet, consectetur adipiscing elit. Vestibulum lacinia eros eu pharetra mollis. Nullam vulputate purus mi, sed maximus est sodales mollis. Mauris nec vulputate eros. Cras lectus lacus, lacinia. Lorem ipsum dolor sit amet, consectetur adipiscing elit. Vestibulum lacinia eros eu pharetra mollis.</div>
  <div class="foot"><span class="brand">Harrowfield<br>Engines</span><i class="foot-rule"></i><div class="foot-band"><span class="circ">Not For Circulation</span><span class="num">7</span></div></div>
</section>

<!-- 8: Biographies -->
<section class="slide" style="left:609px;top:1716px" aria-label="Biographies slide">
  <div class="slide-title" style="top:36px">Heading For Biographies</div>
  <div class="abs" style="left:33px;top:85px;width:224px">
    <div class="sub-head">Name, Title</div>
    <div class="body-text" style="margin-top:3px;font-size:5px"><p>Lorem ipsum dolor sit amet, consectetur adipiscing elit. Vestibulum lacinia eros eu pharetra mollis. Nullam vulputate purus mi, sed maximus est sodales mollis. Mauris nec vulputate eros. Cras lectus lacus, lacinia eu dapibus ac, tincidunt eu nisi. Suspendisse in volutpat risus. Nunc pharetra porttitor lorem. Vivamus at lectus sit amet lacus dictum tincidunt at vel magna. Donec blandit nulla ac erat condimentum, fringilla feugiat ex porttitor. Proin est odio, suscipit vitae magna at, bibendum tincidunt mi. Aenean facilisis pharetra lacus sed tempus. Nam finibus eu diam eu consectetur. Donec blandit nulla ac erat condimentum, fringilla feugiat ex porttitor. Proin est odio, suscipit vitae magna at, bibendum tincidunt mi. Aenean facilisis pharetra lacus sed tempus. Nam finibus eu diam eu consectetur.</p></div>
    <div class="sub-head" style="margin-top:10px">Another Name, Another Title</div>
    <div class="body-text" style="margin-top:3px;font-size:5px"><p>Lorem ipsum dolor sit amet, consectetur adipiscing elit. Vestibulum lacinia eros eu pharetra mollis. Nullam vulputate purus mi, sed maximus est sodales mollis. Mauris nec vulputate eros. Cras lectus lacus, lacinia eu dapibus ac, tincidunt eu nisi.</p></div>
  </div>
  <div class="body-text abs" style="left:283px;top:99px;width:224px;font-size:5px">
    <p>Lorem ipsum dolor sit amet, consectetur adipiscing elit. Vestibulum lacinia eros eu pharetra mollis. Nullam vulputate purus mi, sed maximus est sodales mollis. Mauris nec vulputate eros. Cras lectus lacus, lacinia eu dapibus ac, tincidunt eu nisi. Suspendisse in volutpat risus. Nunc pharetra porttitor lorem. Vivamus at lectus sit amet lacus dictum tincidunt at vel magna. Donec blandit nulla ac erat condimentum, fringilla feugiat ex porttitor. Proin est odio, suscipit vitae magna at, bibendum tincidunt mi. Aenean facilisis pharetra lacus sed tempus. Nam finibus eu diam eu consectetur.</p>
    <p>Lorem ipsum dolor sit amet, consectetur adipiscing elit. Vestibulum lacinia eros eu pharetra mollis. Nullam vulputate purus mi, sed maximus est sodales mollis. Mauris nec vulputate eros. Cras lectus lacus, lacinia eu dapibus ac, tincidunt eu nisi. Suspendisse in volutpat risus. Nunc pharetra porttitor lorem. Vivamus at lectus sit amet lacus dictum tincidunt at vel magna. Donec blandit nulla ac erat condimentum, fringilla feugiat ex porttitor. Proin est odio, suscipit vitae magna at, bibendum tincidunt mi. Aenean facilisis pharetra lacus sed tempus. Nam finibus eu diam eu consectetur.</p>
  </div>
  <div class="foot"><span class="brand">Harrowfield<br>Engines</span><i class="foot-rule"></i><div class="foot-band"><span class="circ">Not For Circulation</span><span class="num">8</span></div></div>
</section>

<!-- 9: Biographies, two columns -->
<section class="slide" style="left:51px;top:2037px" aria-label="Biographies slide">
  <div class="slide-title" style="top:36px">Heading For Biographies</div>
  <div class="abs" style="left:33px;top:85px;width:224px">
    <div class="sub-head">Another Name, Another Title</div>
    <div class="body-text" style="margin-top:3px;font-size:5px"><p>Lorem ipsum dolor sit amet, consectetur adipiscing elit. Vestibulum lacinia eros eu pharetra mollis. Nullam vulputate purus mi, sed maximus est sodales mollis. Mauris nec vulputate eros. Cras lectus lacus, lacinia eu dapibus ac, tincidunt eu nisi. Suspendisse in volutpat risus. Nunc pharetra porttitor lorem. Vivamus at lectus sit amet lacus dictum tincidunt at vel magna. Donec blandit nulla ac erat condimentum, fringilla feugiat ex porttitor. Proin est odio, suscipit vitae magna at, bibendum tincidunt mi. Aenean facilisis pharetra lacus sed tempus. Nam finibus eu diam eu consectetur. Donec blandit nulla ac erat condimentum, fringilla feugiat ex porttitor. Proin est odio, suscipit vitae magna at, bibendum tincidunt mi. Aenean facilisis pharetra lacus sed tempus. Nam finibus eu diam eu consectetur.</p><p>Lorem ipsum dolor sit amet, consectetur adipiscing elit. Vestibulum lacinia eros eu pharetra mollis. Nullam vulputate purus mi, sed maximus est sodales mollis. Mauris nec vulputate eros. Cras lectus lacus, lacinia eu dapibus ac, tincidunt eu nisi. Suspendisse in volutpat risus. Nunc pharetra porttitor lorem. Vivamus at lectus sit amet lacus dictum tincidunt at vel magna. Donec blandit nulla ac erat condimentum.</p></div>
  </div>
  <div class="abs" style="left:283px;top:85px;width:224px">
    <div class="sub-head">Another Name, Another Title</div>
    <div class="body-text" style="margin-top:3px;font-size:5px"><p>Lorem ipsum dolor sit amet, consectetur adipiscing elit. Vestibulum lacinia eros eu pharetra mollis. Nullam vulputate purus mi, sed maximus est sodales mollis. Mauris nec vulputate eros. Cras lectus lacus, lacinia eu dapibus ac, tincidunt eu nisi. Suspendisse in volutpat risus. Nunc pharetra porttitor lorem. Vivamus at lectus sit amet lacus dictum tincidunt at vel magna. Donec blandit nulla ac erat condimentum, fringilla feugiat ex porttitor. Proin est odio, suscipit vitae magna at, bibendum tincidunt mi. Aenean facilisis pharetra lacus sed tempus. Nam finibus eu diam eu consectetur. Donec blandit nulla ac erat condimentum, fringilla feugiat ex porttitor. Proin est odio, suscipit vitae magna at, bibendum tincidunt mi. Aenean facilisis pharetra lacus sed tempus. Nam finibus eu diam eu consectetur.</p><p>Lorem ipsum dolor sit amet, consectetur adipiscing elit. Vestibulum lacinia eros eu pharetra mollis. Nullam vulputate purus mi, sed maximus est sodales mollis. Mauris nec vulputate eros. Cras lectus lacus, lacinia eu dapibus ac, tincidunt eu nisi. Suspendisse in volutpat risus. Nunc pharetra porttitor lorem. Vivamus at lectus sit amet lacus dictum tincidunt at vel magna. Donec blandit nulla ac erat condimentum.</p></div>
  </div>
  <div class="foot"><span class="brand">Harrowfield<br>Engines</span><i class="foot-rule"></i><div class="foot-band"><span class="circ">Not For Circulation</span><span class="num">9</span></div></div>
</section>

<!-- 10: Contact -->
<section class="slide" style="left:609px;top:2037px;background:var(--navy)" aria-label="Contact slide">
  <div class="photo" role="img" aria-label="Photograph of a business handshake with a faint network backdrop"
       style="background:linear-gradient(120deg,var(--navy-deep),#2d6399 55%,#7fa3c6 80%,#3f6f9f)"></div>
  <div class="brand abs" style="left:58px;top:110px;color:#fff;font-size:12px">Harrowfield<br>Engines</div>
  <div class="contact" style="top:171px;font-family:'Roboto',sans-serif;font-weight:700;font-size:12px">Contact Us</div>
  <div class="contact" style="top:199px">
    <div class="contact-row"><svg width="9" height="9" viewBox="0 0 24 24"><path d="M6.6 10.8a15 15 0 0 0 6.6 6.6l2.2-2.2a1 1 0 0 1 1-.25 11 11 0 0 0 3.6.6 1 1 0 0 1 1 1V20a1 1 0 0 1-1 1A17 17 0 0 1 3 4a1 1 0 0 1 1-1h3.5a1 1 0 0 1 1 1 11 11 0 0 0 .6 3.6 1 1 0 0 1-.25 1z" fill="#fff"/></svg>Contact Number Goes Here</div>
    <div class="contact-row"><span style="font-weight:600;font-size:10px;width:9px">@</span>E-Mail Address Goes Here</div>
    <div class="contact-row"><svg width="9" height="9" viewBox="0 0 24 24" fill="none" stroke="#fff" stroke-width="1.6"><circle cx="12" cy="12" r="10"/><ellipse cx="12" cy="12" rx="4.5" ry="10"/><line x1="2" y1="12" x2="22" y2="12"/></svg>URL Address Goes Here</div>
  </div>
  <div class="abs" style="left:0;right:0;top:286px;text-align:center;color:#c8d6e6;font-size:4.6px">© 2021 Harrowfield Engines. All rights reserved.</div>
</section>

</body>
</html>
```